KORMAB Development is an idea development firm. This business card is for Grand Pitchside League, a site that allows users from all over the world to play fantasy cricket against each other.
We need a business card for GPL using our logo and its associated colors. The cards are for the two founders, Marcus Holloway and Peter Lindqvorn. We would like our own cards.
We are handing our card to potential investors and sponsors of our site. It needs to be unique (like our brand.)
Updates
I wanted to thank everyone for their awesome designs!!! It was a hard choice - we narrowed it down to 7 then to three then to 1. All of you are extremely talented - THANK YOU.
Target Market(s)
Potential Investors, Partners
Industry/Entity Type
Business
Contact Information for Business Card
Kormab Development : Grand Pitchside League
Marcus Holloway
Founder
555-204-7731
marcus@kormab.example
www.grandpitchsideleague.example
....
Peter Lindqvorn
Founder
555-618-2940
peter@kormab.example
Look and feel
Each slider illustrates characteristics of the customer's brand and the style your logo design should communicate.

```html
<!DOCTYPE html>
<html lang="en">
<head>
<meta charset="utf-8">
<title>Grand Pitchside League – Business Card</title>
<link rel="stylesheet" href="https://fonts.googleapis.com/css2?family=Open+Sans:wght@300;400;600;700&display=swap">
<style>
  :root{
    --bg:#d9d9d9;
    --green-light:#8fe01c;
    --green:#5cc412;
    --green-dark:#3a9a0c;
    --charcoal:#333436;
    --white:#ffffff;
    --ink:#1f2a1a;
  }
  *{box-sizing:border-box;margin:0;padding:0}
  html,body{width:1200px;height:908px;overflow:hidden}
  body{background:radial-gradient(circle at 50% 40%,#ececec,var(--bg));font-family:"Open Sans",sans-serif;position:relative}
  .card{position:absolute;left:300px;width:600px;height:340px;overflow:hidden;box-shadow:0 10px 24px rgba(0,0,0,.25)}
  .card--front{top:70px;background:radial-gradient(circle at 50% 50%,var(--green-light),var(--green) 60%,var(--green-dark))}
  .card--front .frame{position:absolute;inset:26px;border:6px solid var(--white)}
  .brand{position:absolute;display:flex;align-items:center;gap:12px;white-space:nowrap}
  .brand__mark{width:46px;height:46px;border-radius:50%;background:var(--ink);flex:none}
  .brand__name{font-size:22px;font-weight:400;color:var(--ink);line-height:1}
  .brand__tagline{font-size:9px;color:var(--ink);margin-top:4px}
  .card--front .brand{left:175px;top:140px}
  .card--back{top:480px;background:linear-gradient(180deg,var(--green-light),var(--green) 55%,var(--green-dark))}
  .card--back .brand{left:28px;top:150px}
  .card--back .brand__mark{width:38px;height:38px}
  .card--back .brand__name{font-size:17px}
  .card--back .brand__tagline{font-size:7.5px}
  .divider{position:absolute;left:0;right:0;top:252px;height:6px;background:var(--white)}
  .base{position:absolute;left:0;right:0;top:258px;bottom:0;background:var(--charcoal)}
  .namebox{position:absolute;left:300px;right:0;top:40px;height:72px;background:var(--charcoal);color:var(--white);padding:12px 22px;white-space:nowrap}
  .namebox__name{font-size:22px;font-weight:700;letter-spacing:.5px;line-height:1.1}
  .namebox__name span{font-weight:300}
  .namebox__role{font-size:15px;font-weight:400;margin-top:4px}
  .contact{position:absolute;left:330px;display:flex;align-items:center;gap:12px;font-size:12px;color:var(--ink);line-height:1.35;white-space:nowrap}
  .contact--light{color:var(--white)}
  .icon{width:28px;height:28px;border-radius:50%;background:var(--white);display:flex;align-items:center;justify-content:center;flex:none}
</style>
</head>
<body>
  <section class="card card--front">
    <div class="frame"></div>
    <div class="brand">
      <div class="brand__mark"></div>
      <div>
        <div class="brand__name">Grand Pitchside League</div>
        <div class="brand__tagline">The world's premier fantasy cricket game</div>
      </div>
    </div>
  </section>

  <section class="card card--back">
    <div class="namebox">
      <div class="namebox__name">MARCUS <span>HOLLOWAY</span></div>
      <div class="namebox__role">Founder</div>
    </div>

    <div class="brand">
      <div class="brand__mark"></div>
      <div>
        <div class="brand__name">Grand Pitchside League</div>
        <div class="brand__tagline">The world's premier fantasy cricket game</div>
      </div>
    </div>

    <div class="contact" style="top:132px">
      <div class="icon"><svg width="14" height="14" viewBox="0 0 24 24"><path fill="#333436" d="M6.6 10.8a15 15 0 0 0 6.6 6.6l2.2-2.2c.3-.3.7-.4 1-.2 1.1.4 2.3.6 3.6.6.6 0 1 .4 1 1V20c0 .6-.4 1-1 1A17 17 0 0 1 3 4c0-.6.4-1 1-1h3.5c.6 0 1 .4 1 1 0 1.3.2 2.5.6 3.6.1.3 0 .7-.2 1z"/></svg></div>
      <div>555-204-7731</div>
    </div>
    <div class="contact" style="top:185px">
      <div class="icon"><svg width="16" height="16" viewBox="0 0 24 24" fill="none" stroke="#333436" stroke-width="2"><circle cx="12" cy="12" r="9"/><path d="M3 12h18M12 3c3 3 3 15 0 18M12 3c-3 3-3 15 0 18"/></svg></div>
      <div>marcus@kormab.example<br>www.grandpitchsideleague.example</div>
    </div>
    <div class="divider"></div>
    <div class="base"></div>
    <div class="contact contact--light" style="top:272px">
      <div class="icon"><svg width="14" height="14" viewBox="0 0 24 24"><path fill="#333436" d="M12 2a7 7 0 0 0-7 7c0 5 7 13 7 13s7-8 7-13a7 7 0 0 0-7-7zm0 9.5A2.5 2.5 0 1 1 12 6.5a2.5 2.5 0 0 1 0 5z"/></svg></div>
      <div>Kormab Development<br>Grand Pitchside League</div>
    </div>
  </section>
</body>
</html>
```